Tech Savy small Business accountant business card design

We need a business card for a new company based in the cloud. We provide tax, business advisory, accounting, information technology solutions and back office functions to small businesses. We offer fixed fee packages with add on services as you need them. By harnessing technology we simplify small business operational processes providing valuable time and information for small business owners to grow their business. In the logo (quilbrook) we want to be able to see quil and experts. The final design should communicate achieving growth dreams and balance (ie life and $).
Updates
This project has been temporarily placed on hold until I finalize "Tech Savy small Business accountant needs a logo". I invite all designers to submit on this logo project. Once my logo is finalized I will resume this business card contest. Thanks Added Wednesday, March 19, 2014
This project has been temporarily placed on hold until I finalize "Tech Savy small Business accountant logo". I invite all designers to submit on this logo project. Once my logo is finalized I will resume this business card contest. Thanks Added Thursday, March 20, 2014
Target Market(s)
Small Business (Revenue $500,000, more than 3 employees) owners.
Industry/Entity Type
Small Business
Contact Information for Business Card
Marla Henwick (Principal)
Accountant, Tax Agent.
TEL | 0418 663 904
EMAIL | Marla.Henwick@quilbrook-mail.com.au
WEB | www.quilbrook-mail.com.au
Look and feel

```html
<!DOCTYPE html>
<html lang="en">
<head>
<meta charset="utf-8">
<title>Quilbrook business card</title>
<link rel="stylesheet" href="https://fonts.googleapis.com/css2?family=Open+Sans:wght@400;600;700&display=swap">
<style>
  :root {
    --page: #e9e6e1;
    --card-white: #ffffff;
    --brand-blue: #1e9fd6;
    --band-light: #5fd0ea;
    --band-dark: #1689c2;
    --ink: #3d3f42;
    --muted: #8a8d90;
    --teal: #27b3c9;
    --on-band: #ffffff;
  }
  * { box-sizing: border-box; margin: 0; padding: 0; }
  html, body { width: 1200px; height: 1023px; overflow: hidden; }
  body {
    background: var(--page);
    font-family: "Open Sans", Arial, sans-serif;
    display: flex; align-items: center; justify-content: center;
  }
  .card {
    position: relative;
    width: 900px; height: 550px;
    background: var(--card-white);
    box-shadow: 0 10px 30px rgba(0,0,0,.18);
    overflow: hidden;
  }
  .brand { position: absolute; left: 64px; top: 70px; }
  .brand-name {
    font-weight: 700; font-size: 88px; line-height: 1;
    color: var(--brand-blue); letter-spacing: -2px;
  }
  .brand-tagline {
    margin-top: 6px; margin-left: 8px;
    font-size: 22px; color: var(--muted); letter-spacing: .5px;
  }
  .person { position: absolute; left: 300px; top: 225px; }
  .person-name { font-weight: 600; font-size: 34px; color: var(--ink); }
  .person-title { font-size: 26px; color: var(--teal); margin-left: 70px; }
  .person-rule {
    margin-top: 6px; width: 380px; height: 2px; background: var(--teal);
  }
  .contact-band {
    position: absolute; left: 0; right: 0; top: 345px; bottom: 0;
    background: linear-gradient(100deg, var(--band-light) 0%, #2cb0dd 50%, var(--band-dark) 100%);
  }
  .band-line {
    position: absolute; left: 0; right: 0; top: 12px; height: 2px;
    background: var(--on-band); opacity: .9;
  }
  .contact {
    position: absolute; top: -20px; width: 360px; margin-left: -180px;
    text-align: center; color: var(--on-band);
  }
  .contact-icon {
    display: block; margin: 0 auto 16px;
    width: 66px; height: 66px;
  }
  .contact-text { font-size: 17px; letter-spacing: .3px; }
  .contact-phone { left: 130px; }
  .contact-email { left: 450px; }
  .contact-web { left: 770px; }
</style>
</head>
<body>
  <main class="card">
    <div class="brand">
      <div class="brand-name">quilbrook</div>
      <div class="brand-tagline">Your business and accounting partner</div>
    </div>

    <div class="person">
      <div class="person-name">Marla Henwick (Principal)</div>
      <div class="person-title">Accountant, Tax Agent.</div>
      <div class="person-rule"></div>
    </div>

    <section class="contact-band">
      <div class="band-line"></div>

      <div class="contact contact-phone">
        <svg class="contact-icon" viewBox="0 0 66 66" aria-hidden="true">
          <circle cx="33" cy="33" r="30" fill="#3fbde3" stroke="#fff" stroke-width="3"/>
          <path d="M25 20c2-1 4 0 5 2l2 5c1 2 0 3-1 4l-2 1c1 4 4 7 8 9l1-2c1-1 2-2 4-1l5 2c2 1 3 3 2 5l-1 2c-2 2-5 3-8 2-9-3-15-9-18-18-1-3 0-6 3-8z" fill="#fff"/>
        </svg>
        <div class="contact-text">0418 663 904</div>
      </div>

      <div class="contact contact-email">
        <svg class="contact-icon" viewBox="0 0 66 66" aria-hidden="true">
          <circle cx="33" cy="33" r="30" fill="#34b6df" stroke="#fff" stroke-width="3"/>
          <rect x="19" y="23" width="28" height="20" fill="none" stroke="#fff" stroke-width="2.5"/>
          <path d="M19 23l14 11 14-11M19 43l10-10M47 43L37 33" fill="none" stroke="#fff" stroke-width="2"/>
        </svg>
        <div class="contact-text">Marla.Henwick@quilbrook-mail.com.au</div>
      </div>

      <div class="contact contact-web">
        <svg class="contact-icon" viewBox="0 0 66 66" aria-hidden="true">
          <circle cx="33" cy="33" r="30" fill="#2099cc" stroke="#fff" stroke-width="3"/>
          <g fill="none" stroke="#fff" stroke-width="2">
            <circle cx="33" cy="33" r="13"/>
            <ellipse cx="33" cy="33" rx="6" ry="13"/>
            <path d="M20 33h26M22 26h22M22 40h22M33 20v26"/>
          </g>
        </svg>
        <div class="contact-text">www.quilbrook-mail.com.au</div>
      </div>
    </section>
  </main>
</body>
</html>
```